Web Site - Holloway-Strength.com

Design a 3 page web site for Holloway Strength. See attached design brief.
Holloway Strength - Web Site
www.holloway-strength.com

Design a 3 page web site for Holloway Strength, a small local fitness center that provided cardio and weights only (machines and free weights). There are no classes or other services offered at this facility. Holloway Strength is an affordable alternative to the big box, expensive fitness centers. It is small, local, convenient and a community oriented place to work out.
web site can be clean, simple and communicate basic information about the company and membership offers. Although the branding is black, orange and gray, the web site colors should be soft, light and neutral colors that will appeal to both men and women.
Text: Input generic text during design for each text area that will be modified later during the coding phase. The selected designer is expected to code the site and deliver all compressive files (images, files and code) for an unrestricted hand off and full ownership of all content by the client for future modifications by others.

Images
Images used can be generic royalty free images of people working out, on cardio machines, lifting on universal equipment, stretching or lifting weights or images with out people i.e a yoga mat, free weights, a row of cardio machines etc. This is an adults only facility - images can be a mix of men and women and of diverse multi ethnic backgrounds. Image of the actual gym are included below but should NOT be used on the web site.

Branding - See attached for vertical and horizontal logos for Holloway Strength. These can be used in any way and should be incorporated into the web site
WEB SITE OUTLINE
THREE web pages - Pages can be individual pages clicked through to each page from a navigation area but ALSO pages can be “blend together” into one long scrolling “home” or primary landing page.
1) Home Page with basic information
2) Membership Page (to be later integrated with Quillmark member software to show changing membership specials). - see example below - all text will change later
3) contact page - address - telephone number - google map directions
www.holloway-strength.com
Address:
Located in Tannery Brook Commons
418 E. Walnut Lane, Suite 305, Limerick PA 19468
Tel: 484-555-0172

Target Market(s)

Men and Women - Adults over 18,

Industry/Entity Type

Fitness, Work Out, Gym

Coding

Coded - Design and coding required

Number of Pages Required

3 page

Requirements
Must have
• See Project Brief
Should not have
• Dark Colors that feel too masculine

```html
<!DOCTYPE html>
<html lang="en">
<head>
<meta charset="utf-8">
<title>Holloway Strength</title>
<link href="https://fonts.googleapis.com/css2?family=Michroma&family=Poppins:wght@400;500;600&family=Roboto+Condensed:wght@400;700&display=swap" rel="stylesheet">
<style>
:root{
  --orange:#ff5f0f;
  --orange-soft:#fcd9c3;
  --cream:#fff4ed;
  --ink:#1f1f1f;
  --muted:#555;
  --footer:#2b2b2b;
  --field:#e4e4e4;
}
*{margin:0;padding:0;box-sizing:border-box}
html,body{width:1200px;height:5291px;overflow:hidden}
body{position:relative;background:#fff;font-family:"Poppins",sans-serif;color:var(--ink)}
.abs{position:absolute}
.display{font-family:"Michroma",sans-serif;letter-spacing:1px;font-weight:400}
.accent{color:var(--orange)}
.btn{position:absolute;display:flex;align-items:center;justify-content:center;background:var(--orange);color:#fff;border-radius:40px;font-weight:500;text-transform:uppercase}
.brand{font-family:"Poppins",sans-serif;font-weight:600;color:var(--ink);letter-spacing:2px;line-height:1.15}

/* header */
.site-header{left:0;top:0;width:1200px;height:148px;background:#fff}
.site-header .brand{left:62px;top:50px;font-size:22px;display:flex;align-items:center;gap:12px}
.brand-dot{width:26px;height:26px;border-radius:50%;background:var(--orange);flex:none}
.nav{right:62px;top:54px;display:flex;gap:56px;align-items:center;font-size:16px}
.nav a{color:var(--ink);text-decoration:none}
.nav .active{color:var(--orange)}
.nav .nav-cta{background:var(--orange);color:#fff;padding:9px 20px;border-radius:30px}

/* hero */
.hero{left:0;top:148px;width:1200px;height:785px;background:linear-gradient(180deg,#6d5a48 0%,#3b3029 55%,#211b17 100%)}
.hero-text{left:0;width:1200px;text-align:center;color:#fff;line-height:1}
.hero .welcome{top:455px;font-size:30px;font-weight:500}
.hero .title{top:512px;font-size:46px;color:var(--orange);letter-spacing:2px}
.hero .lead{top:590px;font-size:19px;line-height:28px;left:140px;width:920px}
.hero .btn{left:491px;top:670px;width:216px;height:55px;font-size:19px}

/* about */
.about-accent{left:41px;top:1140px;width:487px;height:540px;background:var(--orange)}
.about-photo{left:68px;top:1112px;width:487px;height:538px;background:linear-gradient(135deg,#8a8580,#4c4743 60%,#2c2826)}
.about-accent2{left:440px;top:1600px;width:90px;height:80px;background:var(--orange);clip-path:polygon(0 0,100% 100%,0 100%)}
.section-title{font-size:44px;line-height:1}
.kicker{font-size:17px;color:var(--orange);display:flex;align-items:center;gap:4px}
.kicker .rule{height:2px;background:var(--orange)}
.about .section-title{left:625px;top:1225px}
.about .kicker{left:625px;top:1286px}
.about p{left:625px;top:1352px;width:510px;font-size:13px;line-height:27.5px;color:var(--muted);text-align:justify}
.about .btn{left:625px;top:1568px;width:200px;height:54px;font-size:17px}

/* membership */
.membership-head{left:0;top:1876px;width:1200px;display:flex;justify-content:center;align-items:center;gap:16px}
.membership-head .rule{width:100px;height:2px;background:var(--orange)}
.membership-head .section-title{font-size:36px}
.membership-sub{left:0;top:1958px;width:1200px;text-align:center;font-size:21px;line-height:28px;color:#333}
.plan{position:absolute;border-radius:24px;background:var(--cream);border:1px solid #f6d3bd;text-align:center}
.plan.featured{background:var(--orange-soft);border:2px solid var(--orange)}
.plan h3{margin-top:38px;font-family:"Michroma",sans-serif;font-weight:400;font-size:21px;letter-spacing:1px}
.plan .price{margin-top:12px;font-size:40px;font-weight:600}
.plan .price small{font-size:16px;font-weight:400}
.plan ul{list-style:none;text-align:left;margin:28px 0 0 65px}
.plan li{display:flex;align-items:center;gap:10px;font-size:15.5px;height:40px}
.plan .btn{left:50%;transform:translateX(-50%);width:124px;height:42px;font-size:13px;font-weight:600}

/* banner */
.banner{left:0;top:2692px;width:1200px;height:600px;background:linear-gradient(180deg,#55504c 0%,#2e2a28 55%,#1c1a19 100%)}
.banner-title{left:0;width:1200px;text-align:center;color:#fff;font-family:"Roboto Condensed",sans-serif;font-size:74px;line-height:1}
.banner .b1{top:295px;font-weight:700}
.banner .b2{top:383px;font-weight:400}
.banner .btn{left:471px;top:487px;width:259px;height:62px;font-size:23px}

/* gallery */
.gallery-head{left:0;top:3420px;width:1200px;text-align:center}
.gallery-head .kicker{justify-content:center;margin-top:14px}
.tile{position:absolute}
.dots{left:562px;top:4188px;display:flex;gap:12px}
.dots span{width:9px;height:9px;border-radius:50%;background:#f7b996}
.dots span:first-child{background:var(--orange)}

/* contact */
.contact-photo{left:596px;top:4274px;width:604px;height:586px;background:linear-gradient(90deg,#ffffff 0%,#d8d8da 35%,#6d6f75 70%,#3c3e44 100%)}
.contact .section-title{left:64px;top:4305px}
.contact .kicker{left:72px;top:4372px}
.contact .note{left:64px;top:4432px;font-size:13px;color:#333}
.field{position:absolute;border:1px solid var(--field);font-size:11.5px;color:#555;padding:14px 18px}
.contact .btn{left:66px;top:4739px;width:218px;height:67px;font-size:18px;font-weight:600}

/* footer */
.site-footer{left:0;top:4897px;width:1200px;height:394px;background:var(--footer);color:#fff}
.footer-title{font-family:"Michroma",sans-serif;font-size:20px;letter-spacing:1px}
.quick{left:226px;top:70px}
.quick ul{list-style:none;margin-top:30px}
.quick li{display:flex;align-items:center;gap:10px;font-size:13px;height:32px}
.footer-brand{left:480px;top:130px;width:240px;text-align:center;color:#fff;font-size:24px}
.social{left:548px;top:268px;display:flex;gap:12px}
.social span{width:32px;height:32px;border:2px solid #fff;border-radius:50%}
.footer-contact{left:824px;top:70px}
.fc-item{position:absolute;left:0;display:flex;gap:18px;font-size:12.5px;line-height:16px;width:300px}
.fc-icon{width:26px;height:26px;border:1.5px solid var(--orange);display:flex;align-items:center;justify-content:center;flex:none}
.footer-rule{left:66px;top:320px;width:1064px;height:1px;background:var(--orange)}
.copyright{left:0;top:342px;width:1200px;text-align:center;font-size:12px}
</style>
</head>
<body>

<header class="abs site-header">
  <div class="abs brand"><span class="brand-dot"></span>HOLLOWAY<br>STRENGTH</div>
  <nav class="abs nav">
    <a class="active" href="#">Home</a><a href="#">About Us</a><a href="#">Membership</a><a href="#">Gallery</a><a class="nav-cta" href="#">Contact Us</a>
  </nav>
</header>

<section class="abs hero" role="img" aria-label="Trainer with clipboard coaching a member on a leg press machine">
  <div class="abs hero-text welcome">Welcome To</div>
  <div class="abs hero-text title display">HOLLOWAY STRENGTH</div>
  <p class="abs hero-text lead">Lorem ipsum dolor sit amet, consectetur adipiscing elit, sed do eiusmod tempor incididunt ut labore et dolore magna aliqua. Quis ipsum suspendisse ultrices gravida.</p>
  <a class="btn">Contact Us</a>
</section>

<section class="about">
  <div class="abs about-accent"></div>
  <div class="abs about-photo" role="img" aria-label="Woman training on a rowing machine with people exercising behind her"></div>
  <div class="abs about-accent2"></div>
  <h2 class="abs section-title display">ABOUT <span class="accent">US</span></h2>
  <div class="abs kicker">WHO WE ARE<span class="rule" style="width:100px"></span></div>
  <p class="abs">Lorem ipsum dolor sit amet, consectetur adipiscing elit, sed do eiusmod tempor incididunt ut labore et dolore magna aliqua. Quis ipsum suspendisse ultrices gravida. Risus commodo viverra maecenas accumsan lacus vel faci lisis. Lorem ipsum dolor sit amet, consectetur adipiscing elit, sed do eiusmod tempor incidid unt ut labore et dolore magna aliqua. Quis ipsum susp endisse ultrices gravida. Risus commodo viverra maecenas accumsan lacus vel facilisis.</p>
  <a class="btn">Know More</a>
</section>

<section class="membership">
  <div class="abs membership-head"><span class="rule"></span><h2 class="section-title display">HOLLOWAY <span class="accent">MEMBERSHIP</span></h2><span class="rule"></span></div>
  <p class="abs membership-sub">Choose perfect plans to match your fitness goals<br>and start your journey today</p>

  <svg width="0" height="0" style="position:absolute"><defs><symbol id="tick" viewBox="0 0 16 16"><circle cx="8" cy="8" r="8" fill="#ff5f0f"/><path d="M4.5 8.3l2.3 2.3 4.7-4.9" fill="none" stroke="#fff" stroke-width="1.8"/></symbol></defs></svg>

  <div class="plan" style="left:82px;top:2110px;width:317px;height:459px">
    <h3>BASIC PLAN</h3>
    <div class="price">$ 19.00/<small>Month</small></div>
    <ul>
      <li><svg width="16" height="16"><use href="#tick"/></svg>Single Personalized Plan</li>
      <li><svg width="16" height="16"><use href="#tick"/></svg>Tailored To Fitness Goals</li>
      <li><svg width="16" height="16"><use href="#tick"/></svg>Basic Workouts</li>
      <li><svg width="16" height="16"><use href="#tick"/></svg>Meal Suggestions</li>
      <li><svg width="16" height="16"><use href="#tick"/></svg>Email Support</li>
    </ul>
    <a class="btn" style="top:377px">Join Now</a>
  </div>

  <div class="plan featured" style="left:423px;top:2080px;width:360px;height:520px">
    <h3>PRO PLAN</h3>
    <div class="price">39.00/<small>Month</small></div>
    <ul style="margin-left:85px">
      <li><svg width="16" height="16"><use href="#tick"/></svg>Personal Training</li>
      <li><svg width="16" height="16"><use href="#tick"/></svg>Weight Tracking</li>
      <li><svg width="16" height="16"><use href="#tick"/></svg>Basic Workouts</li>
      <li><svg width="16" height="16"><use href="#tick"/></svg>Meal Suggestions</li>
      <li><svg width="16" height="16"><use href="#tick"/></svg>Progress Monitoring</li>
      <li><svg width="16" height="16"><use href="#tick"/></svg>Email Support</li>
    </ul>
    <a class="btn" style="top:456px">Join Now</a>
  </div>

  <div class="plan" style="left:804px;top:2110px;width:317px;height:459px">
    <h3>ELITE PLAN</h3>
    <div class="price">79.00/<small>Month</small></div>
    <ul>
      <li><svg width="16" height="16"><use href="#tick"/></svg>All Pro Plan Features</li>
      <li><svg width="16" height="16"><use href="#tick"/></svg>One-On-One Coaching</li>
      <li><svg width="16" height="16"><use href="#tick"/></svg>Weekly Check- Ins</li>
      <li><svg width="16" height="16"><use href="#tick"/></svg>Meal Suggestions</li>
      <li><svg width="16" height="16"><use href="#tick"/></svg>Email Support</li>
    </ul>
    <a class="btn" style="top:377px">Join Now</a>
  </div>
</section>

<section class="abs banner" role="img" aria-label="Woman lifting a dumbbell and man doing rows in a dark gym">
  <div class="abs banner-title b1">EXPERIENCE FITNESS</div>
  <div class="abs banner-title b2">LIKE NEVER BEFORE</div>
  <a class="btn">Contact Us</a>
</section>

<section class="gallery">
  <div class="abs gallery-head">
    <h2 class="section-title display">OUR <span class="accent">GALLERY</span></h2>
    <div class="kicker"><span class="rule" style="width:105px"></span>&nbsp;PORTFOLIO&nbsp;<span class="rule" style="width:105px"></span></div>
  </div>
  <div class="tile" style="left:64px;top:3621px;width:312px;height:222px;background:linear-gradient(135deg,#d9d6d2,#6b625a)" role="img" aria-label="Man and woman training on exercise machines"></div>
  <div class="tile" style="left:64px;top:3861px;width:312px;height:222px;background:linear-gradient(135deg,#a8a39c,#4e4944)" role="img" aria-label="Trainer assisting a member on a leg press"></div>
  <div class="tile" style="left:397px;top:3621px;width:407px;height:462px;background:linear-gradient(160deg,#b9b5ae,#57534e 70%,#38352f)" role="img" aria-label="Man and woman doing lunges with dumbbells"></div>
  <div class="tile" style="left:824px;top:3621px;width:312px;height:222px;background:linear-gradient(135deg,#8b7c6e,#3a322c)" role="img" aria-label="Group training on rowing machines"></div>
  <div class="tile" style="left:824px;top:3861px;width:312px;height:222px;background:linear-gradient(135deg,#c4c0bb,#5e5954)" role="img" aria-label="Group lifting barbells in a class"></div>
  <div class="abs dots"><span></span><span></span><span></span><span></span></div>
</section>

<section class="contact">
  <div class="abs contact-photo" role="img" aria-label="Man working out with dumbbells in a gym, fading into white"></div>
  <h2 class="abs section-title display">CONTACT <span class="accent">US</span></h2>
  <div class="abs kicker">HOLLOWAY STRENGTH<span class="rule" style="width:100px"></span></div>
  <p class="abs note">Please fill out the form below and click submit to contact us. Thank you!</p>
  <div class="field" style="left:64px;top:4517px;width:232px;height:45px">Your Name</div>
  <div class="field" style="left:312px;top:4517px;width:232px;height:45px">Phone Number</div>
  <div class="field" style="left:64px;top:4574px;width:480px;height:42px">Email Address</div>
  <div class="field" style="left:64px;top:4628px;width:480px;height:76px">Message</div>
  <a class="btn">Submit Now</a>
</section>

<footer class="abs site-footer">
  <div class="abs quick">
    <div class="footer-title">QUICK <span class="accent">LINKS</span></div>
    <ul>
      <li><svg width="16" height="16" viewBox="0 0 16 16"><path d="M3 8h9M8.5 4l4 4-4 4" fill="none" stroke="#ff5f0f" stroke-width="2"/></svg>About Us</li>
      <li><svg width="16" height="16" viewBox="0 0 16 16"><path d="M3 8h9M8.5 4l4 4-4 4" fill="none" stroke="#ff5f0f" stroke-width="2"/></svg>Membership</li>
      <li><svg width="16" height="16" viewBox="0 0 16 16"><path d="M3 8h9M8.5 4l4 4-4 4" fill="none" stroke="#ff5f0f" stroke-width="2"/></svg>Gallery</li>
      <li><svg width="16" height="16" viewBox="0 0 16 16"><path d="M3 8h9M8.5 4l4 4-4 4" fill="none" stroke="#ff5f0f" stroke-width="2"/></svg>Testimonials</li>
      <li><svg width="16" height="16" viewBox="0 0 16 16"><path d="M3 8h9M8.5 4l4 4-4 4" fill="none" stroke="#ff5f0f" stroke-width="2"/></svg>Contact Us</li>
    </ul>
  </div>
  <div class="abs brand footer-brand" style="color:#fff">HOLLOWAY<br>STRENGTH</div>
  <div class="abs social" aria-label="Social profiles"><span></span><span></span><span></span></div>
  <div class="abs footer-contact">
    <div class="footer-title">CONTACT <span class="accent">US</span></div>
    <div class="fc-item" style="top:78px"><span class="fc-icon"><svg width="14" height="14" viewBox="0 0 16 16"><path d="M4 2l3 3-2 2c1 2 2 3 4 4l2-2 3 3-2 2C7 14 2 9 2 4z" fill="#ff5f0f"/></svg></span><span>CALL US<br>484 555 0172</span></div>
    <div class="fc-item" style="top:133px"><span class="fc-icon"><svg width="14" height="14" viewBox="0 0 16 16"><rect x="2" y="4" width="12" height="9" fill="#ff5f0f"/><path d="M2 4l6 5 6-5" fill="none" stroke="#2b2b2b" stroke-width="1.2"/></svg></span><span>EMAIL US<br>info@holloway-strength.com</span></div>
    <div class="fc-item" style="top:182px"><span class="fc-icon"><svg width="14" height="14" viewBox="0 0 16 16"><path d="M8 1a5 5 0 0 1 5 5c0 4-5 9-5 9S3 10 3 6a5 5 0 0 1 5-5z" fill="#ff5f0f"/><circle cx="8" cy="6" r="2" fill="#2b2b2b"/></svg></span><span>Address line Dummy Here<br>Address line Here</span></div>
  </div>
  <div class="abs footer-rule"></div>
  <div class="abs copyright">Copyright ©2026 All rights reserved by the company name</div>
</footer>

</body>
</html>
```